Business website cyber security

Full redesign of our current business website, mockup and powerpoint presentation have been provided.
Some animated elements (example: SVG with CSS) are welcome.
A detailed requirement list can also be found in the attached powerpoint
Also uploaded is the current page as a nicepage & html export. All 11 sites shall be reworked. "Branches", "Download", "Contact" and "Legal Information" are not needed .

A good example of a competitor is https://www.brantvolo.de/ this. Not in terms of colors, but in regard to website structure, animated elements and overall look.

Target Market(s)

Cyber security for the B2B market

Industry/Entity Type

IT, IT Security, banking

Coding

Coded - Design and coding required

Number of Pages Required

5+ page

Font styles to use
Other font styles liked:
• ReadexPro Regular, ReadexPro Light

Colors
0054AA
0677BA
7BADD7
CADEEF
E8F1F8

Requirements
Must have
• Modern and sleek design, corporate identity
Nice to have
• Animated elements (css svg)
Should not have
• too many colors (max 4), too fancy

```html
<!DOCTYPE html>
<html lang="de">
<head>
<meta charset="utf-8">
<title>Kerval – IT Security · Compliance</title>
<link href="https://fonts.googleapis.com/css2?family=Readex+Pro:wght@300;400;500;600&family=Saira:wght@300;400;600;700&display=swap" rel="stylesheet">
<style>
:root{
  --navy:#0a2565;
  --deep:#0c2f7c;
  --mid:#12409a;
  --royal:#0054AA;
  --accent:#3f8fe2;
  --sky:#7BADD7;
  --pale:#CADEEF;
  --white:#E8F1F8;
  --line:rgba(123,173,215,.55);
}
*{margin:0;padding:0;box-sizing:border-box}
html,body{width:1200px;height:4392px;overflow:hidden}
body{position:relative;background:var(--navy);color:var(--white);font-family:"Readex Pro",sans-serif}
.abs{position:absolute}
.display{font-family:"Saira",sans-serif;text-transform:uppercase}
.bg-top{left:0;top:0;width:1200px;height:1824px;background:linear-gradient(180deg,#0b2f7e 0%,#11409a 45%,#1648a4 100%)}
.bg-mid{left:0;top:1824px;width:1200px;height:2200px;background:linear-gradient(180deg,#10378a 0%,#0c2e78 50%,#0b2a6e 100%)}
.bg-foot{left:0;top:4024px;width:1200px;height:368px;background:#0a2463}

/* nav */
.brand{left:105px;top:3px;width:130px;height:130px;border-radius:50%;border:2px solid var(--pale);background:var(--navy);display:flex;align-items:center;justify-content:center;font-family:"Readex Pro",sans-serif;font-weight:600;font-size:22px;letter-spacing:1px;color:#fff}
.nav{left:305px;top:38px;display:flex;gap:39px;font-size:12px;letter-spacing:.4px}
.nav a{color:#fff;text-decoration:none;position:relative}
.nav a.active::after{content:"";position:absolute;left:0;right:0;top:26px;height:2px;background:#fff}
.lang{left:1026px;top:39px;width:26px;height:16px;background:var(--pale);border-radius:2px}
.nav-rule{left:0;top:92px;width:1200px;height:1px;background:rgba(123,173,215,.25)}

/* hero */
.hero-art{left:494px;top:102px;width:706px;height:563px;border-radius:0 0 0 280px;background:radial-gradient(circle at 45% 55%,#e83a6a 0%,#6a2fb5 14%,#1f5fd0 34%,#0e3a95 62%,rgba(11,47,126,0) 80%)}
.hero-sub{left:123px;top:258px;font-size:35px;font-weight:300;color:var(--accent);line-height:40px}
.hero-h{left:123px;top:298px;font-size:35px;font-weight:600;line-height:42px;color:#fff}
.hero-p{left:125px;top:397px;width:380px;font-size:12px;line-height:19.5px}
.btn{display:flex;align-items:center;justify-content:center;background:var(--accent);color:#fff;font-size:13px;font-weight:600;letter-spacing:1px;text-transform:uppercase}
.hero-btn{left:128px;top:506px;width:179px;height:42px}

/* service cards */
.card{top:745px;width:299px;height:223px;border:1.5px solid var(--line);text-align:center;padding:0 36px}
.card h3{font-size:16px;font-weight:600;letter-spacing:.6px;line-height:19px;margin-top:56px;text-transform:uppercase}
.card p{font-size:11px;line-height:19px;margin-top:10px;color:var(--pale)}
.card-icon{top:-36px;left:116px;width:66px;height:66px;border-radius:50%;background:radial-gradient(circle,#2e6fd0 0%,#15449c 65%,rgba(21,68,156,0) 100%)}

/* vision */
.eyebrow{font-family:"Saira",sans-serif;text-transform:uppercase;color:var(--accent);font-size:15px;font-weight:300;width:1200px;text-align:center}
.sec-title{font-family:"Saira",sans-serif;text-transform:uppercase;font-weight:600;font-size:37px;letter-spacing:1.5px;width:1200px;text-align:center;color:#fff}
.tabs{left:319px;top:1176px;width:610px;display:flex;font-size:16px;font-weight:500}
.tabs span{flex:1;text-align:center}
.tabs-rule{left:319px;top:1214px;width:610px;height:1px;background:rgba(123,173,215,.35)}
.tabs-active{left:319px;top:1212px;width:200px;height:4px;background:var(--accent)}
.orbit{left:112px;top:1291px;width:464px;height:464px;border-radius:50%;border:1.5px solid rgba(123,173,215,.6)}
.orbit-inner{left:146px;top:1325px;width:396px;height:396px;border-radius:50%;background:radial-gradient(circle at 50% 45%,#2a8ae8 0%,#1260c6 40%,#0b3c92 80%,#0a2f7e 100%)}
.vis-h{left:629px;top:1318px;font-size:26px;font-weight:600;line-height:34px}
.vis-h em{font-style:normal;color:var(--accent)}
.vis-p{left:629px;top:1400px;width:440px;font-size:11.5px;line-height:19px}
.vis-lead{left:629px;top:1470px;font-size:12px;font-weight:600}
.feat{top:1514px;font-size:12.5px;font-weight:600;line-height:19px}
.feat svg{display:block;margin-bottom:6px}
.vis-note{left:629px;top:1638px;width:470px;font-size:11.5px;line-height:19px}

/* branches */
.br-p{left:250px;top:1967px;width:700px;font-size:13px;line-height:19px;text-align:center}
.tile{top:2090px;height:263px}
.tile-label{position:absolute;left:0;right:0;bottom:20px;text-align:center;font-family:"Saira",sans-serif;text-transform:uppercase;font-weight:600;font-size:18px;line-height:20px}
.tile-label span{font-weight:400;display:block}
.tile-active{left:227px;top:2060px;width:261px;height:324px;background:linear-gradient(180deg,rgba(56,138,228,.96),rgba(30,104,210,.96));text-align:center}
.tile-active h4{font-family:"Saira",sans-serif;text-transform:uppercase;font-size:20px;font-weight:600;line-height:22px;margin-top:58px}
.tile-active h4 span{font-weight:300;display:block}
.tile-active ul{list-style:none;width:160px;margin:18px auto 0;font-size:13px}
.tile-active li{padding:5px 0;border-bottom:1px solid rgba(232,241,248,.45)}
.tile-active li:last-child{border:none}
.chev{margin:16px auto 0;width:34px;height:34px;border-radius:50%;border:1.5px solid #fff}

/* team */
.team-art{left:580px;top:2425px;width:620px;height:479px;border-radius:240px 0 0 240px;border:2px solid var(--accent);border-right:none;background:radial-gradient(circle at 42% 50%,#5fb5ff 0%,#1f6fd8 30%,#0c3c96 70%,#0a2c76 100%)}
.team-eyebrow{left:143px;top:2515px;font-family:"Saira",sans-serif;color:var(--accent);font-size:18px;font-weight:300;text-transform:uppercase}
.team-h{left:140px;top:2545px;font-family:"Saira",sans-serif;text-transform:uppercase;font-size:37px;font-weight:600;letter-spacing:1px}
.team-q{left:140px;top:2613px;width:400px;font-size:18px;line-height:22px}
.team-p{left:140px;top:2672px;width:400px;font-size:16.5px;line-height:22px}
.team-btn{left:140px;top:2791px;width:189px;height:45px}
.stem{left:596px;top:2907px;width:1px;height:74px;background:var(--sky)}
.stem-dot{left:593px;top:2979px;width:7px;height:7px;border-radius:50%;background:var(--sky)}

/* partners */
.partner{font-size:26px;font-weight:400;color:var(--sky);transform:translateX(-50%);white-space:nowrap;display:flex;align-items:center;gap:8px}
.partner i{display:inline-block;width:22px;height:22px;background:var(--sky)}

/* news */
.news-line{left:0;top:3617px;width:74px;height:1px;background:var(--sky)}
.news-dot{left:72px;top:3614px;width:7px;height:7px;border-radius:50%;background:var(--sky)}
.news-eyebrow{left:121px;top:3603px;font-family:"Saira",sans-serif;color:var(--accent);font-size:17px;font-weight:300;text-transform:uppercase}
.news-h{left:121px;top:3632px;font-family:"Saira",sans-serif;text-transform:uppercase;font-size:34px;font-weight:600;line-height:36px}
.news-p{left:123px;top:3720px;width:140px;font-size:12.5px;line-height:21px}
.news-btn{left:126px;top:3809px;width:138px;height:38px;font-size:12px}
.post{top:3580px;width:231px;height:311px;background:#0d2f7a;border:1px solid rgba(123,173,215,.35);overflow:hidden}
.post.first{border-bottom:3px solid var(--accent)}
.post-img{height:156px}
.post-date{position:absolute;left:26px;top:150px;background:var(--accent);font-size:9px;padding:3px 10px;border-radius:2px}
.post h5{margin:24px 22px 0;font-size:12.5px;font-weight:600;line-height:16px}
.post p{margin:7px 22px 0;font-size:9.5px;line-height:15px;color:var(--pale)}
.post .more{margin:8px 22px 0;font-size:9.5px;font-weight:600;display:flex;align-items:center;gap:6px}

/* footer */
.foot-brand{left:154px;top:4074px;width:146px;height:146px;border-radius:50%;border:2.5px solid var(--pale);display:flex;align-items:center;justify-content:center;font-weight:600;font-size:24px;letter-spacing:1px}
.vrule{top:4024px;width:1px;height:239px;background:rgba(123,173,215,.35)}
.fcol{top:4080px}
.fcol h6{font-size:13px;font-weight:600;letter-spacing:.5px;text-transform:uppercase;border-left:3px solid var(--accent);padding-left:18px;margin-left:-21px;line-height:18px}
.fcol ul{list-style:none;margin-top:20px;font-size:11.5px;color:var(--pale)}
.fcol li{height:24.7px}
.contact-row{display:flex;align-items:center;gap:14px;margin-top:18px}
.contact-row .ic{width:30px;height:30px;border-radius:50%;background:#fff;display:flex;align-items:center;justify-content:center}
.contact-row small{display:block;font-size:10.5px;color:var(--pale)}
.contact-row b{font-weight:400;font-size:12.5px}
.foot-rule{left:0;top:4305px;width:1200px;height:1px;background:rgba(123,173,215,.25)}
.copy{left:467px;top:4324px;font-size:11px;color:var(--pale)}
.socials{left:924px;top:4316px;display:flex;gap:8px}
.socials span{width:28px;height:28px;border-radius:50%;background:#fff}

@keyframes pulse{0%,100%{opacity:.55}50%{opacity:1}}
.pulse{animation:pulse 3s ease-in-out infinite}
</style>
</head>
<body>
<div class="abs bg-top"></div>
<div class="abs bg-mid"></div>
<div class="abs bg-foot"></div>

<!-- header -->
<div class="abs brand">KERVAL</div>
<nav class="abs nav">
  <a class="active" href="#">CDAAS</a>
  <a href="#">SECURITY SERVICES</a>
  <a href="#">COMPLIANCE</a>
  <a href="#">UNTERNEHMEN</a>
  <a href="#">KARRIERE</a>
  <a href="#">KONTAKT</a>
</nav>
<div class="abs lang"></div>
<svg class="abs" style="left:1058px;top:42px" width="14" height="10" viewBox="0 0 14 10"><path d="M2 2l5 5 5-5" fill="none" stroke="#fff" stroke-width="2"/></svg>
<div class="abs nav-rule"></div>

<!-- hero -->
<div class="abs hero-art pulse" role="img" aria-label="Illustration: vernetzte Cloud-Infrastruktur mit Sicherheitsschloss und Laptop"></div>
<div class="abs hero-sub display">Die IT-Sicherheit Ihrer</div>
<h1 class="abs hero-h display">IT-Infrastruktur ist<br>unsere Mission.</h1>
<p class="abs hero-p">Unsere Cybersicherheitsdienste sind rund um den Kunden konzipiert. Wir bieten eine robuste Zusammenarbeit, um die Herausforderungen Ihrer Umgebung zu verstehen und maßgeschneiderte, sichere Lösungen zu entwickeln.</p>
<div class="abs btn hero-btn">Learn more</div>

<!-- service cards -->
<div class="abs card" style="left:145px">
  <div class="abs card-icon"><svg width="66" height="66" viewBox="0 0 66 66"><path d="M33 17l13 5v10c0 9-6 15-13 18-7-3-13-9-13-18V22z" fill="none" stroke="#fff" stroke-width="2"/><rect x="28" y="31" width="10" height="8" fill="#fff"/><path d="M30 31v-3a3 3 0 016 0v3" fill="none" stroke="#fff" stroke-width="2"/></svg></div>
  <h3>CDaaS Cyber Defense as a Service</h3>
  <p>Unser All-in-One CDaaS-Angebot, bietet eine komfortable Integration ihrer IT-Infrastruktur in eine aktive und umfassende Sicherheitslösung.</p>
</div>
<div class="abs card" style="left:453px;top:745px">
  <div class="abs card-icon" style="top:-44px"><svg width="66" height="66" viewBox="0 0 66 66"><path d="M33 14l11 4v8c0 7-5 11-11 14-6-3-11-7-11-14v-8z" fill="none" stroke="#fff" stroke-width="2"/><path d="M18 46h14l8-5" fill="none" stroke="#fff" stroke-width="2"/><path d="M28 27l4 4 7-7" fill="none" stroke="#fff" stroke-width="2"/></svg></div>
  <h3 style="margin-top:50px">Security Services</h3>
  <p>Unsere Security Services unterstützen Sie umfassend in der Planung und Umsetzung zu ihrem ganzheitlichen IT- und Informationsmanagement.</p>
</div>
<div class="abs card" style="left:760px">
  <div class="abs card-icon"><svg width="66" height="66" viewBox="0 0 66 66"><rect x="22" y="16" width="22" height="30" fill="none" stroke="#fff" stroke-width="2"/><path d="M26 24h4M26 31h4M26 38h4M33 24h7M33 31h7M33 38h7" stroke="#fff" stroke-width="2"/></svg></div>
  <h3 style="margin-top:58px">Compliance</h3>
  <p>Wir unterstützen Sie rund um Ihre IT-Sicherheit auf höchstem Niveau mit einer effektiven Compliance-Strategie.</p>
</div>

<!-- vision & mission -->
<div class="abs eyebrow" style="left:0;top:1073px">Darum die Kerval S.à r.l</div>
<h2 class="abs sec-title" style="left:0;top:1095px">Vision &amp; Mission</h2>
<div class="abs tabs"><span>VISION</span><span>MISSION</span><span>PORTFOLIO</span></div>
<div class="abs tabs-rule"></div>
<div class="abs tabs-active"></div>

<div class="abs orbit"></div>
<div class="abs orbit-inner pulse" role="img" aria-label="Illustration: Schutzschild vor einem Laptop mit Datenpunkten"></div>

<h3 class="abs vis-h display">Ganzheitliche IT-Sicherheit<br>ist unser <em>Anspruch</em></h3>
<p class="abs vis-p">Wir stehen für Ihre IT-Sicherheit. Wir bieten umfangreiche Services und unsere zertifizierten IT-Expertinnen und Experten sorgen gemeinsam mit Ihnen dafür, dass Ihre Systeme sicher werden.</p>
<p class="abs vis-lead">Mit uns haben Sie:</p>
<div class="abs feat" style="left:636px">
  <svg width="42" height="36" viewBox="0 0 42 36"><circle cx="21" cy="18" r="15" fill="none" stroke="#fff" stroke-width="2"/><text x="21" y="22" font-size="10" fill="#fff" text-anchor="middle" font-family="Readex Pro, sans-serif">24</text></svg>
  Schnellste<br>Reaktionszeiten 24x7
</div>
<div class="abs feat" style="left:801px">
  <svg width="42" height="36" viewBox="0 0 42 36"><rect x="11" y="7" width="20" height="20" fill="none" stroke="#fff" stroke-width="2"/><rect x="17" y="13" width="8" height="8" fill="#fff"/><path d="M15 3v4M21 3v4M27 3v4M15 27v4M21 27v4M27 27v4M7 12h4M7 22h4M31 12h4M31 22h4" stroke="#fff" stroke-width="2"/></svg>
  Marktführende<br>Technologien
</div>
<div class="abs feat" style="left:938px">
  <svg width="42" height="36" viewBox="0 0 42 36"><circle cx="21" cy="15" r="9" fill="none" stroke="#fff" stroke-width="2"/><path d="M16 23l-3 10 8-4 8 4-3-10" fill="none" stroke="#fff" stroke-width="2"/><path d="M17 15l3 3 5-5" fill="none" stroke="#fff" stroke-width="2"/></svg>
  Zertifizierte Cyber-<br>Analystinnen und Analysten<br>mit höchster Expertise
</div>
<p class="abs vis-note">Das Pay-As-You-Grow“-Modell erlaubt eine laufende Anpassung der in Anspruch genommenen Professional Security Services – mit einem Anspruch: Ihren Bedarf.</p>

<!-- branches -->
<div class="abs eyebrow" style="left:0;top:1877px">Industry Branches</div>
<h2 class="abs sec-title" style="left:0;top:1895px">Branchen</h2>
<p class="abs br-p">Wir stehen für Ihre IT-Sicherheit. Wir bieten umfangreiche Services und unsere zertifizierten IT-Expertinnen und Experten sorgen gemeinsam mit Ihnen dafür, dass Ihre Systeme sicher werden.</p>

<div class="abs tile" style="left:0;width:227px;background:linear-gradient(160deg,#2a3f66,#101d38)" role="img" aria-label="Foto: Finanzberater vor einer Datenwand"><div class="tile-label">Financial<span>Sectors</span></div></div>
<div class="abs tile" style="left:488px;width:235px;background:linear-gradient(180deg,#16233f,#8a5a2c 70%,#d07a2c)" role="img" aria-label="Foto: Stadt bei Nacht mit leuchtenden Lichtern"><div class="tile-label">Energy</div></div>
<div class="abs tile" style="left:723px;width:235px;background:linear-gradient(160deg,#3f86c8,#16406f)" role="img" aria-label="Foto: Ingenieur an einem holografischen Fahrzeugmodell"><div class="tile-label">Automobil<span>Industrie</span></div></div>
<div class="abs tile" style="left:958px;width:236px;background:linear-gradient(160deg,#8a8f96,#5c4e3a)" role="img" aria-label="Foto: Lagerarbeiterin in einem Logistikzentrum"><div class="tile-label">Logistics</div></div>
<div class="abs tile-active">
  <h4>IT Service<span>Ops</span></h4>
  <ul><li>Event Management</li><li>Incident Management</li><li>Request Fulfillment</li><li>Access Management</li></ul>
  <div class="chev"><svg width="31" height="31" viewBox="0 0 31 31"><path d="M10 13l5.5 5.5L21 13" fill="none" stroke="#fff" stroke-width="2"/></svg></div>
</div>

<!-- team -->
<div class="abs team-art pulse" role="img" aria-label="Illustration: digitales Sicherheitsschild mit Vorhängeschloss"></div>
<div class="abs team-eyebrow">Professional Team</div>
<h2 class="abs team-h">Arbeiten bei Kerval</h2>
<p class="abs team-q">"Wir setzen auf Vertrauen, Zuverlässigkeit und Professionalität"</p>
<p class="abs team-p">Lorem ipsum dolor sit amet, consectetur adipiscing elit, sed do eiusmod tempor incididunt ut labore et dolore magna aliqua. Ut enim ad minim veniam, quis nostrud exercitatio</p>
<div class="abs btn team-btn">Learn more</div>
<div class="abs stem"></div>
<div class="abs stem-dot"></div>

<!-- partners -->
<div class="abs eyebrow" style="left:0;top:3035px">Our Partners</div>
<h2 class="abs sec-title" style="left:0;top:3053px">Produkte &amp; Partner</h2>
<div class="abs partner" style="left:205px;top:3200px">Alvera</div>
<div class="abs partner" style="left:402px;top:3200px"><i></i>Quillmark</div>
<div class="abs partner" style="left:597px;top:3200px;font-size:16px">Ledgerline · Cirrano</div>
<div class="abs partner" style="left:805px;top:3200px">Vapora</div>
<div class="abs partner" style="left:997px;top:3200px">Lumetric</div>
<div class="abs partner" style="left:198px;top:3324px">Tracewell</div>
<div class="abs partner" style="left:401px;top:3324px">Hostrel</div>
<div class="abs partner" style="left:607px;top:3324px">Sentiro</div>
<div class="abs partner" style="left:808px;top:3328px;font-size:19px">Guardlane</div>
<div class="abs partner" style="left:1009px;top:3328px;font-size:19px">Radiex</div>

<!-- news -->
<div class="abs news-line"></div>
<div class="abs news-dot"></div>
<div class="abs news-eyebrow">News &amp; Blog</div>
<h2 class="abs news-h">Our latest<br>news</h2>
<p class="abs news-p">Lorem ipsum dolor sit amet, consectetur adipiscing elit</p>
<div class="abs btn news-btn">View more</div>

<article class="abs post first" style="left:373px">
  <div class="post-img" style="background:linear-gradient(160deg,#6d87a8,#24426f)" role="img" aria-label="Foto: Geschäftsmann mit Sicherheitssymbolen"></div>
  <span class="post-date">AUG 20, 2022</span>
  <h5>Lorem ipsum dolor sit amet, consectetur adipiscing</h5>
  <p>Lorem ipsum dolor sit amet, consectetur adipiscing elit, sed do eiusmo</p>
  <div class="more">LEARN MORE <svg width="16" height="8" viewBox="0 0 16 8"><path d="M0 4h14M11 1l3 3-3 3" fill="none" stroke="#fff"/></svg></div>
</article>
<article class="abs post" style="left:621px">
  <div class="post-img" style="background:linear-gradient(160deg,#2fb0f0,#1a3f9c)" role="img" aria-label="Illustration: Schutzschild über Laptop"></div>
  <span class="post-date">AUG 20, 2022</span>
  <h5>Lorem ipsum dolor sit amet, consectetur adipiscing</h5>
  <p>Lorem ipsum dolor sit amet, consectetur adipiscing elit, sed do eiusmo</p>
  <div class="more">LEARN MORE <svg width="16" height="8" viewBox="0 0 16 8"><path d="M0 4h14M11 1l3 3-3 3" fill="none" stroke="#fff"/></svg></div>
</article>
<article class="abs post" style="left:868px">
  <div class="post-img" style="background:linear-gradient(160deg,#4f7fb4,#1b335c)" role="img" aria-label="Foto: Hände auf einer Tastatur mit Datenüberlagerung"></div>
  <span class="post-date">AUG 20, 2022</span>
  <h5>Lorem ipsum dolor sit amet, consectetur adipiscing</h5>
  <p>Lorem ipsum dolor sit amet, consectetur adipiscing elit, sed do eiusmo</p>
  <div class="more">LEARN MORE <svg width="16" height="8" viewBox="0 0 16 8"><path d="M0 4h14M11 1l3 3-3 3" fill="none" stroke="#fff"/></svg></div>
</article>
<article class="abs post" style="left:1115px">
  <div class="post-img" style="background:linear-gradient(160deg,#3aa4ee,#1a4aa0)" role="img" aria-label="Illustration: digitale Sicherheitsgrafik"></div>
  <span class="post-date">AUG 20, 2022</span>
  <h5>Lorem ipsum dolor sit amet, consectetur adipiscing</h5>
  <p>Lorem ipsum dolor sit amet, consectetur adipiscing elit, sed do eiusmo</p>
  <div class="more">LEARN MORE</div>
</article>

<!-- footer -->
<div class="abs foot-brand">KERVAL</div>
<div class="abs vrule" style="left:411px"></div>
<div class="abs vrule" style="left:650px"></div>
<div class="abs vrule" style="left:842px"></div>
<div class="abs fcol" style="left:432px">
  <h6>Navigation</h6>
  <ul><li>Cdaas</li><li>Security Services</li><li>Compliance</li><li>Unternehmen</li><li>Career</li></ul>
</div>
<div class="abs fcol" style="left:667px">
  <h6>Resources</h6>
  <ul style="margin-top:24px"><li>Terms &amp; Condition</li><li>Privacy Policy</li><li>Blogs</li><li>Contact Us</li></ul>
</div>
<div class="abs fcol" style="left:877px">
  <h6>Contact Us</h6>
  <div class="contact-row" style="margin-top:22px">
    <span class="ic"><svg width="16" height="16" viewBox="0 0 16 16"><path d="M3 1l3 3-2 2c1 2 3 4 5 5l2-2 3 3-2 3C6 14 2 10 1 3z" fill="#0a2463"/></svg></span>
    <span><small>Phone Number</small><b>+352 2740 11 55 - 20</b></span>
  </div>
  <div class="contact-row">
    <span class="ic"><svg width="16" height="12" viewBox="0 0 16 12"><rect x="1" y="1" width="14" height="10" fill="none" stroke="#0a2463" stroke-width="1.6"/><path d="M1 1l7 6 7-6" fill="none" stroke="#0a2463" stroke-width="1.6"/></svg></span>
    <span><small>Email us</small><b>contact@kerval-sec.lu</b></span>
  </div>
</div>
<div class="abs foot-rule"></div>
<div class="abs copy">Copyright © 2022 Kerval. All Rights Reserved</div>
<div class="abs socials"><span></span><span></span><span></span><span></span></div>
</body>
</html>
```